Need eye catching business card for Growing IT Cybersecurity services company

Business card design for 20 year IT consulting company that has created a new logo.

We would like the business card design to be attention-grabbing, unique, clean and modern, professional.

Ideally, we want to be humanized by including a photo. Also open to other ideas to make the cards stand out (ie include personal likes or something perhaps).

Target Market(s)

Businesses needing cybersecurity, managed IT services and consulting.

Industry/Entity Type

Technology

Contact Information for Business Card

Name, Title, email, phone, website

Requirements
Must have
• Please include QR code - DOUBLE-SIDED; section won't save for some reason
Should not have
• Note that the graphic back_r2.jpg is the OLD LOGO. But this contains the core values of the organization that would be good to include in the design.

```html
<!DOCTYPE html>
<html lang="en">
<head>
<meta charset="utf-8">
<title>Northgrid Technical – Business Card</title>
<link href="https://fonts.googleapis.com/css2?family=Montserrat:wght@400;500;700;800&display=swap" rel="stylesheet">
<style>
  :root {
    --navy: #0a4068;
    --orange: #e2821f;
    --paper: #f1f2f3;
    --ghost: #dde2e6;
    --ink: #3b3f44;
    --white: #ffffff;
    --stage: #2b2c2e;
  }
  * { margin: 0; padding: 0; box-sizing: border-box; }
  html, body { width: 1200px; height: 900px; overflow: hidden; }
  body {
    background: var(--stage);
    font-family: "Montserrat", sans-serif;
    position: relative;
  }
  .card {
    position: absolute;
    left: 250px;
    width: 700px;
    height: 400px;
    background: var(--paper);
    overflow: hidden;
    box-shadow: 0 10px 30px rgba(0,0,0,.45);
  }
  .card--front { top: 40px; }
  .card--back { top: 470px; }
  .card-shapes { position: absolute; inset: 0; width: 700px; height: 400px; }

  .brand {
    position: absolute;
    left: 34px;
    top: 34px;
    display: flex;
    align-items: center;
    gap: 14px;
  }
  .brand-dot {
    width: 58px; height: 58px;
    border-radius: 50%;
    background: var(--navy);
  }
  .brand-name {
    font-weight: 800;
    font-size: 34px;
    line-height: 1;
    letter-spacing: 1px;
    color: var(--navy);
    text-transform: uppercase;
  }

  .tagline {
    position: absolute;
    left: 40px;
    top: 150px;
    font-weight: 700;
    font-size: 19px;
    color: var(--navy);
  }
  .services {
    position: absolute;
    left: 40px;
    top: 232px;
    list-style: none;
    color: var(--white);
    font-size: 17px;
    font-weight: 500;
    line-height: 26px;
  }
  .services li { display: flex; align-items: center; gap: 10px; }
  .services svg { width: 14px; height: 14px; flex: none; }
  .slogan {
    position: absolute;
    right: 40px;
    top: 315px;
    font-weight: 800;
    font-size: 26px;
    color: var(--white);
  }

  .photo-slot {
    position: absolute;
    left: 0; top: 250px;
    width: 380px; height: 150px;
    display: flex; align-items: center; justify-content: center;
    color: var(--white);
    font-weight: 800;
    font-size: 30px;
  }
  .person {
    position: absolute;
    left: 400px;
    top: 160px;
    color: var(--ink);
  }
  .person-name { font-weight: 800; font-size: 22px; color: var(--navy); letter-spacing: .5px; }
  .person-title { font-size: 17px; margin-top: 2px; }
  .contact-line {
    display: flex; align-items: center; gap: 8px;
    font-size: 17px; margin-top: 6px;
    white-space: nowrap;
  }
  .contact-line svg { width: 16px; height: 16px; flex: none; }
  .contact-band {
    position: absolute;
    left: 400px;
    top: 276px;
    width: 285px;
    color: var(--navy);
  }
  .contact-band .contact-line { font-size: 17px; margin-top: 8px; }
</style>
</head>
<body>

  <section class="card card--front" aria-label="Business card front">
    <svg class="card-shapes" viewBox="0 0 700 400" aria-hidden="true">
      <circle cx="560" cy="120" r="150" fill="var(--ghost)" opacity=".6"/>
      <rect x="400" y="255" width="300" height="145" fill="var(--orange)"/>
      <path d="M0 206 H330 Q446 206 446 322 V400 H0 Z" fill="var(--orange)"/>
      <path d="M0 214 H328 Q438 214 438 324 V400 H0 Z" fill="var(--navy)"/>
    </svg>
    <div class="brand">
      <span class="brand-dot"></span>
      <span class="brand-name">Northgrid Technical</span>
    </div>
    <p class="tagline">Business Technology Management</p>
    <ul class="services">
      <li><svg viewBox="0 0 14 14"><path d="M1 8 L5 12 L13 2" stroke="var(--orange)" stroke-width="2.4" fill="none"/></svg>Managed IT Services</li>
      <li><svg viewBox="0 0 14 14"><path d="M1 8 L5 12 L13 2" stroke="var(--orange)" stroke-width="2.4" fill="none"/></svg>Cloud Computing</li>
      <li><svg viewBox="0 0 14 14"><path d="M1 8 L5 12 L13 2" stroke="var(--orange)" stroke-width="2.4" fill="none"/></svg>VoIP Phone Systems</li>
      <li><svg viewBox="0 0 14 14"><path d="M1 8 L5 12 L13 2" stroke="var(--orange)" stroke-width="2.4" fill="none"/></svg>Data Analytics</li>
      <li><svg viewBox="0 0 14 14"><path d="M1 8 L5 12 L13 2" stroke="var(--orange)" stroke-width="2.4" fill="none"/></svg>Co-Managed IT</li>
      <li><svg viewBox="0 0 14 14"><path d="M1 8 L5 12 L13 2" stroke="var(--orange)" stroke-width="2.4" fill="none"/></svg>Cybersecurity</li>
    </ul>
    <p class="slogan">We'er here to help!</p>
  </section>

  <section class="card card--back" aria-label="Business card back">
    <svg class="card-shapes" viewBox="0 0 700 400" aria-hidden="true">
      <circle cx="560" cy="110" r="150" fill="var(--ghost)" opacity=".6"/>
      <rect x="380" y="262" width="320" height="138" fill="var(--orange)"/>
      <path d="M0 242 H270 Q386 242 386 358 V400 H0 Z" fill="var(--orange)"/>
      <path d="M0 250 H268 Q378 250 378 360 V400 H0 Z" fill="var(--navy)"/>
    </svg>
    <div class="brand">
      <span class="brand-dot"></span>
      <span class="brand-name">Northgrid Technical</span>
    </div>
    <div class="photo-slot" role="img" aria-label="Portrait photo of the card holder goes here">Photo Here</div>
    <div class="person">
      <p class="person-name">MARK DORLAND</p>
      <p class="person-title">Chief Revenue Officer</p>
      <p class="contact-line">
        <svg viewBox="0 0 16 16"><rect x="4" y="1" width="8" height="14" rx="1.5" fill="none" stroke="var(--orange)" stroke-width="1.6"/></svg>
        (555) 343-0182
      </p>
    </div>
    <div class="contact-band">
      <p class="contact-line">
        <svg viewBox="0 0 16 16"><path d="M2 6 Q8 1 14 6 L12 8 L10 6 H6 L4 8 Z M4 9 H12 V14 H4 Z" fill="var(--navy)"/></svg>
        (555) 620-0147
      </p>
      <p class="contact-line">
        <svg viewBox="0 0 16 16"><rect x="1" y="3" width="14" height="10" rx="1.5" fill="var(--navy)"/><path d="M1.5 4 L8 9 L14.5 4" stroke="var(--orange)" stroke-width="1.3" fill="none"/></svg>
        mark@ngtech.io
      </p>
      <p class="contact-line">
        <svg viewBox="0 0 16 16"><circle cx="8" cy="8" r="6.5" fill="none" stroke="var(--navy)" stroke-width="1.6"/><path d="M1.5 8 H14.5 M8 1.5 Q4 8 8 14.5 M8 1.5 Q12 8 8 14.5" stroke="var(--navy)" stroke-width="1.2" fill="none"/></svg>
        www.ngtech.io
      </p>
    </div>
  </section>

</body>
</html>
```